Northgate Roofing Works Inc Business cards

Commercial and Residential Roofing contractor needs design logo and card design. Can be single or double sided but must incorporate:
Persons Name:
Persons Title:
Mailing Address: PO Box 3719
Physical Address: 58 Fenwick Lane
Harlow Falls, Ma. 01692
800-316-5842
508-712-5842
Fax: 508-712-5867
Cell: Person Cell number
email address
Website: WWW.northgateroofworks.com

Target Market(s)

Residential home owners and commercial building owners

Industry/Entity Type

Roofing

Contact Information for Business Card

Persons Name:
Persons Title:
Harlow Falls, Ma. 01692
800-316-5842
508-712-5842
Fax: 508-712-5867
Cell: Person Cell number
email address

Logo Text

Large enough to service small enough to care

Font styles to use
Serif

Colors
0355a3

Requirements
Must have
• Commercial and Residential Roofing contractor needs design logo and card design. Can be single or double sided but must incorporate:
• Persons Name:
• Persons Title:
• Mailing Address: PO Box 3719
• Physical Address: 58 Fenwick Lane
• Harlow Falls, Ma. 01692
• 800-316-5842
• 508-712-5842
• Fax: 508-712-5867
• Cell: Person Cell number
• email address
• Website: WWW.northgateroofworks.com
Nice to have
• ..
Should not have
• I'm looking for something different. I have had the same card for 23 years. I attached what both sides of my present card looks like.

```html
<!DOCTYPE html>
<html lang="en">
<head>
<meta charset="utf-8">
<title>Northgate Roofing Works Inc – Business Cards</title>
<link rel="stylesheet" href="https://fonts.googleapis.com/css2?family=Libre+Baskerville&family=Questrial&display=swap">
<style>
  :root {
    --brand-blue: #0355a3;
    --front-blue: #1d5ea8;
    --logo-grey: #b9bcc0;
    --text-grey: #6d6f72;
    --band-grey: #c9cbce;
    --card-white: #f7f8f9;
    --backdrop: #e4e1dc;
  }
  * { box-sizing: border-box; margin: 0; padding: 0; }
  html, body { width: 1200px; height: 800px; overflow: hidden; }
  body {
    background: var(--backdrop);
    font-family: "Questrial", sans-serif;
    position: relative;
  }
  .card {
    position: absolute;
    width: 540px;
    height: 309px;
    border-radius: 3px;
    box-shadow: 0 10px 28px rgba(0,0,0,.22);
    overflow: hidden;
  }
  /* Front */
  .card-front {
    left: 40px; top: 246px;
    background: var(--front-blue);
    display: flex; align-items: center; justify-content: center;
  }
  .brand-front { display: flex; align-items: center; gap: 14px; }
  .brand-front .brand-square { width: 46px; height: 46px; background: var(--logo-grey); }
  .brand-front .brand-name {
    font-size: 34px; color: var(--logo-grey); letter-spacing: .5px; white-space: nowrap;
  }
  /* Back */
  .card-back { left: 620px; top: 246px; background: var(--card-white); }
  .holder { position: absolute; right: 40px; top: 36px; text-align: right; }
  .holder-name {
    font-family: "Libre Baskerville", serif;
    font-size: 26px; color: var(--brand-blue); line-height: 1.1; white-space: nowrap;
  }
  .holder-title { font-size: 13px; color: var(--text-grey); margin-top: 4px; }

  .brand-back { position: absolute; left: 34px; top: 146px; display: flex; align-items: center; gap: 8px; }
  .brand-back .brand-square { width: 22px; height: 22px; background: var(--brand-blue); }
  .brand-back .brand-name { font-size: 17px; color: var(--brand-blue); white-space: nowrap; }

  .contact {
    position: absolute;
    display: grid;
    grid-template-columns: auto auto;
    column-gap: 6px;
    font-size: 11.5px; line-height: 19px;
    color: var(--text-grey);
    white-space: nowrap;
  }
  .contact dt { color: var(--brand-blue); font-weight: 700; grid-column: 1; }
  .contact dd { grid-column: 2; }
  .contact-direct { left: 290px; top: 114px; }
  .contact-address { left: 34px; top: 184px; }

  .edge-band { position: absolute; left: 0; bottom: 0; width: 100%; height: 20px; }
</style>
</head>
<body>
  <section class="card card-front" aria-label="Card front">
    <div class="brand-front">
      <span class="brand-square"></span>
      <span class="brand-name">northgate roofing</span>
    </div>
  </section>

  <section class="card card-back" aria-label="Card back">
    <div class="holder">
      <p class="holder-name">Grant Halloway</p>
      <p class="holder-title">President</p>
    </div>

    <dl class="contact contact-direct">
      <dt>Fax:</dt><dd>508-712-5867</dd>
      <dt>Cell:</dt><dd>508-604-2281</dd>
      <dt>Email:</dt><dd>grant@northgateroofworks.com</dd>
      <dt>Website:</dt><dd>www.northgateroofworks.com</dd>
    </dl>

    <div class="brand-back">
      <span class="brand-square"></span>
      <span class="brand-name">northgate roofing</span>
    </div>

    <dl class="contact contact-address">
      <dt>Mailing Address:</dt><dd>PO Box 3719</dd>
      <dt>Physical Address:</dt><dd>58 Fenwick Lane</dd>
      <dd>Harlow Falls, Ma. 01692</dd>
      <dd>800-316-5842</dd>
      <dd>508-712-5842</dd>
    </dl>

    <svg class="edge-band" viewBox="0 0 540 20" preserveAspectRatio="none" aria-hidden="true">
      <polygon points="0,0 236,0 226,20 0,20" fill="var(--brand-blue)"/>
      <polygon points="240,0 540,0 540,20 230,20" fill="var(--band-grey)"/>
    </svg>
  </section>
</body>
</html>
```